OVRIN Website Design

A professional website is needed for OVRIN, a newly developed entity that helps support the Professional Employer Organization (PEO) industry through web-based systems. These systems are designed to help PEOs comply with regulatory compliance requirements and to facilitate the completion of online state application and renewal forms.

PEOs serve small and medium-sized businesses by handling tasks related to employee payroll, state/federal tax payments, health & WC insurance, and employment law compliance. (Learn more about PEOs from http://www.tolvarhub.example/business/peo-services). Because PEOs take on such significant responsibilities for other businesses, many U.S. states require PEO licensing and bonding.

OVRIN was founded to help these PEOs and states increase the efficiency/reliability of this state oversight process through its web-based systems.

Target Market(s)

PEO Industry representatives and state/federal industry regulators

Industry/Entity Type

Industry

Requirements
Must have
• This is a "design-only" job; no coding is needed. Website should be clean and professional with colors that are compatible with the uploaded logo (green/cream). Additional items:

1. The home page design needs to incorporate (a) OVRIN logo (uploaded), (b) descriptive text (below), and (c) images for OVRIN's 3 alliance partners.

2. The site's interior pages (also design only/no coding) should include (a) a header with the OVRIN logo, (b) footer (for items such as a privacy policy, VELSKO logo, etc), (c) vertical menu of links specific to each service

Primary text for home page:

PEO regulatory compliance made easier … better!
➢ Increase efficiency and reliability of registration/licensing
➢ Reduce errors, omissions and late filings
➢ Save time and money

The OVRIN Alliance
➢ PEO Industry Partners
➢ PEOs
➢ State Regulatory Agencies

Join the Team!

```html
<!DOCTYPE html>
<html lang="en">
<head>
<meta charset="utf-8">
<title>OVRIN – PEO regulatory compliance</title>
<link rel="stylesheet" href="https://fonts.googleapis.com/css2?family=Arimo:ital,wght@0,400;0,700;1,400&display=swap">
<style>
:root{
  --green:#3aa51b;
  --green-dark:#2f9e0c;
  --green-light:#53b32f;
  --ink:#222;
  --grey-text:#555;
  --muted:#9a9a9a;
  --bg:#ececec;
  --panel-line:#a9a9a9;
  --arrow:#8cc4ea;
}
*{box-sizing:border-box;margin:0;padding:0}
html,body{width:1130px;height:1200px;overflow:hidden}
body{font-family:"Arimo",Arial,sans-serif;color:var(--ink);background:var(--bg);position:relative}
.page-backdrop{position:absolute;inset:0;width:1130px;height:1200px}
.brand{position:absolute;left:45px;top:30px;display:flex;align-items:center;gap:14px}
.brand-mark{width:26px;height:26px;background:var(--green)}
.brand-name{font-size:58px;font-weight:700;color:#4a4a4a;letter-spacing:2px;line-height:1}
.social{position:absolute;right:28px;top:35px;display:flex;gap:14px}
.social span{width:50px;height:50px;border-radius:6px;background:#9aa3ab}
.main-nav{position:absolute;top:138px;left:0;width:1130px;height:34px}
.main-nav a{position:absolute;font-size:20px;font-weight:700;color:var(--green);text-decoration:none;white-space:nowrap}
.main-nav a.current{color:#3a3a3a}
.hero{position:absolute;left:0;top:173px;width:1130px;height:357px;
  background:linear-gradient(90deg,#6b5d55 0%,#8d8580 25%,#d5d3d0 45%,#e6e3df 55%,#2b2c31 70%,#1c1d22 100%)}
.hero-title{position:absolute;left:65px;top:60px;font-size:49px;line-height:56px;color:#fff;font-weight:400;text-shadow:0 2px 6px rgba(0,0,0,.45)}
.alliance-title{position:absolute;left:70px;width:252px;top:575px;text-align:center;font-size:22px;font-weight:700;color:var(--green)}
.banner-frame{position:absolute;left:70px;top:613px;width:252px;height:256px;border:2px solid #bdbdbd;border-radius:6px;background:#e7e7e7}
.banner{position:absolute;left:10px;width:230px;height:70px;border-radius:3px;display:flex;align-items:center;justify-content:center;font-size:19px;color:#333}
.banner.one{top:8px;background:linear-gradient(160deg,#cfe0f4,#7ea9e2)}
.banner.two{top:88px;background:linear-gradient(180deg,#fafafa,#dcdcdc)}
.banner.three{top:168px;background:linear-gradient(160deg,#fde8b0,#f5b46a)}
.support{position:absolute;left:63px;top:912px;z-index:2}
.support-title{font-size:21px;line-height:24px;color:var(--green)}
.support-phone{margin-top:12px;font-size:34px;color:var(--muted);margin-left:-6px;white-space:nowrap}
.support-mail{margin-top:4px;font-size:19px;color:#2f8a2f;margin-left:3px;white-space:nowrap}
.support-figure{position:absolute;left:302px;top:912px;width:50px;height:163px;border-radius:26px 26px 8px 8px;background:linear-gradient(180deg,#c7c7c7,#d8d8d8);z-index:1}
.benefits{position:absolute;left:412px;top:570px;list-style:none}
.benefits li{display:flex;align-items:center;height:53px;font-size:24px;font-style:italic;color:#1c1c1c}
.benefits svg{width:36px;height:32px;margin-right:12px}
.content-panel{position:absolute;left:413px;top:743px;width:680px;height:326px;border:2px solid var(--panel-line);border-radius:6px;background:linear-gradient(180deg,#ececec,#f6f6f6)}
.article{position:absolute;left:10px;width:650px}
.article h3{font-size:17px;font-weight:400;color:var(--green)}
.article p{font-size:14px;line-height:18px;color:#111}
.steps{display:flex;margin-top:8px}
.step{display:flex;width:290px;align-items:flex-start}
.step-num{font-size:46px;line-height:40px;color:#c8c8c8;width:30px}
.step-text{font-size:15px;line-height:19px;color:var(--muted);width:230px;padding-top:2px}
.sample{position:absolute;right:8px;top:138px;font-size:19px;color:#222}
.divider{position:absolute;left:84px;top:1112px;width:961px;height:2px;background:#c9c9c9}
.site-footer{position:absolute;left:0;top:1120px;width:1130px;height:80px;display:flex}
.footer-left{width:597px;background:var(--green-light);color:#fff;font-size:16px;padding:35px 0 0 40px}
.footer-right{flex:1;background:var(--green-dark)}
</style>
</head>
<body>
<svg class="page-backdrop" viewBox="0 0 1130 1200" aria-hidden="true">
  <rect width="1130" height="1200" fill="#ebebeb"/>
  <path d="M0 0 Q60 110 110 160 L0 160Z" fill="#f2f2f2"/>
  <path d="M250 560 Q900 500 1130 1150 L1130 560Z" fill="#f1f1f1"/>
  <rect x="0" y="0" width="1130" height="170" fill="#f3f3f3"/>
</svg>

<header>
  <div class="brand"><span class="brand-mark"></span><span class="brand-name">OVRIN</span></div>
  <div class="social" aria-label="Social links"><span></span><span></span><span></span></div>
  <nav class="main-nav">
    <a class="current" href="#" style="left:86px">Home</a>
    <a href="#" style="left:312px">About</a>
    <a href="#" style="left:528px">Services</a>
    <a href="#" style="left:729px">Privacy Policy</a>
    <a href="#" style="left:971px">Contact us</a>
  </nav>
</header>

<section class="hero" role="img" aria-label="Photo of a business presenter pointing at a bar chart during a meeting">
  <h1 class="hero-title">PEO regulatory<br>compliance made easier…<br>better!</h1>
</section>

<aside>
  <h2 class="alliance-title">The OVRIN Alliance</h2>
  <div class="banner-frame">
    <div class="banner one" role="img" aria-label="Partner banner"></div>
    <div class="banner two">links/banners</div>
    <div class="banner three" role="img" aria-label="Partner banner"></div>
  </div>
  <div class="support">
    <div class="support-title">Supportum Tecnicum<br>dit possibolo</div>
    <div class="support-phone">1-800-555-014</div>
    <div class="support-mail">help@ovrin.example</div>
  </div>
  <div class="support-figure" role="img" aria-label="Silhouette of a support representative"></div>
</aside>

<ul class="benefits">
  <li><svg viewBox="0 0 36 32"><path d="M2 10h16V2l16 14-16 14v-8H2z" fill="var(--arrow)"/></svg>Increase efficiency and reliability of registration/licensing</li>
  <li><svg viewBox="0 0 36 32"><path d="M2 10h16V2l16 14-16 14v-8H2z" fill="var(--arrow)"/></svg>Reduce errors, omissions and late filings</li>
  <li><svg viewBox="0 0 36 32"><path d="M2 10h16V2l16 14-16 14v-8H2z" fill="var(--arrow)"/></svg>Save time and money</li>
</ul>

<section class="content-panel">
  <article class="article" style="top:8px">
    <h3>Pellentesque eleifend</h3>
    <p>Dolor in elementum mollis, urna velit dignissim nisi, at tincidunt ipsum mi quis ante. Quisque iaculis egestas velit. Quisque sit amet libero a mauris condimentum hendrerit. Mauris rutrum facilisis dolor. Sed a leo. Aliquam erat volutpat.</p>
    <div class="steps">
      <div class="step"><span class="step-num">1</span><span class="step-text">Dolor in elementum mollis, urna velit dignissim nisi.</span></div>
      <div class="step"><span class="step-num">2</span><span class="step-text">Dolor in elementum mollis, urna velit dignissim nisi.</span></div>
    </div>
  </article>
  <div class="sample">sample text</div>
  <article class="article" style="top:172px">
    <h3>Pellentesque eleifend</h3>
    <p>Dolor in elementum mollis, urna velit dignissim nisi, at tincidunt ipsum mi quis ante. Quisque iaculis egestas velit. Quisque sit amet libero a mauris condimentum hendrerit. Mauris rutrum facilisis dolor. Sed a leo. Aliquam erat volutpat.</p>
    <div class="steps">
      <div class="step"><span class="step-num">1</span><span class="step-text">Dolor in elementum mollis, urna velit dignissim nisi.</span></div>
      <div class="step"><span class="step-num">2</span><span class="step-text">Dolor in elementum mollis, urna velit dignissim nisi.</span></div>
    </div>
  </article>
</section>

<div class="divider"></div>
<footer class="site-footer">
  <div class="footer-left">© OVRIN 2013</div>
  <div class="footer-right"></div>
</footer>
</body>
</html>
```